Selam-Kaveh - Promote and Support a community

Design a website for Ethiopean Community. the design should be friendly, easy to navigate and maintain the look & feel of the Ethiopian culture. a proposed logo is attached but it can be change according to your recommendations. This is a project we are doing at a discount rate as it supports a weak community.
Please visit their current website http://www.selam-kaveh.example.org/index.php?lang=en

Target Market(s)

Community members, potential doners

Industry/Entity Type

community

Number of Pages Required

1 page

Font styles to use
Sans Serif

Requirements
Must have
• easy to navigate friendly interface

```html
<!DOCTYPE html>
<html lang="en">
<head>
<meta charset="utf-8">
<title>Selam Kaveh – Community Health</title>
<link href="https://fonts.googleapis.com/css2?family=Poppins:wght@300;400;500;600;700&family=Crimson+Text:wght@700&display=swap" rel="stylesheet">
<style>
:root{
  --teal:#0b6360;
  --red:#9a0c0c;
  --lime:#cccc2e;
  --ink:#2b2b2b;
  --muted:#666;
  --white:#fff;
}
*{box-sizing:border-box;margin:0;padding:0}
html,body{width:1200px;height:3774px;overflow:hidden}
body{position:relative;font-family:"Poppins",sans-serif;color:var(--ink);background:var(--white)}
.abs{position:absolute}
.eyebrow{font-size:13px;color:var(--lime);letter-spacing:.3px;text-transform:uppercase}
.h2{font-size:36px;font-weight:600;color:var(--red);line-height:1.1}
.body-text{font-size:12.5px;line-height:19.5px;color:var(--muted)}
.pill-btn{display:flex;align-items:center;gap:10px;background:var(--lime);border-radius:22px;font-weight:600;font-size:13px;color:#1f1f1f;padding-left:4px;height:40px}
.pill-btn .ic{width:32px;height:32px;border-radius:50%;background:#fff;display:flex;align-items:center;justify-content:center}
.photo{background:linear-gradient(135deg,#8c7f76,#5d6e86 55%,#b64a4a)}

/* top bar */
.topbar{left:0;top:0;width:1200px;height:40px;background:var(--teal);color:#fff;font-size:12.5px}
.topbar .item{position:absolute;top:11px;display:flex;align-items:center;gap:8px}
/* nav */
.nav{left:0;top:40px;width:1200px;height:65px;background:#fff}
.brand{position:absolute;left:66px;top:6px;display:flex;align-items:center;gap:8px}
.brand .mark{width:54px;height:54px;border-radius:50%;background:var(--red)}
.brand span{font-size:15px;font-weight:600;color:var(--red)}
.menu a{position:absolute;top:27px;font-size:11.5px;color:#555;text-decoration:none;text-transform:uppercase}
.menu a.active{color:var(--red)}
.nav-cta{position:absolute;left:990px;top:13px;width:148px;height:40px}

/* hero */
.hero{left:0;top:105px;width:1200px;height:638px;overflow:hidden}
.hero-kicker{left:170px;top:188px;font-size:13px;color:var(--teal);text-transform:uppercase}
.hero-title{left:170px;top:218px;font-family:"Crimson Text",serif;font-size:54px;line-height:63px;color:#fff;text-shadow:0 2px 6px rgba(0,0,0,.45)}
.hero-cta{left:170px;top:383px;width:148px}
.arrow{width:36px;height:36px;border-radius:50%;background:#fff;display:flex;align-items:center;justify-content:center}

/* about */
.stat-val{font-size:20px;font-weight:600;color:var(--teal)}
.stat-lab{font-size:14px;color:#222}

/* programs */
.prog-card{position:absolute;top:1380px;width:188px;height:264px;border-radius:94px 94px 40px 40px/110px 110px 40px 40px}
.prog-title{position:absolute;top:1648px;font-size:15px;line-height:23px}
.pager{left:567px;top:1742px;font-size:11px;font-weight:600;display:flex;gap:22px;align-items:center}

/* community */
.bullets{left:132px;top:1985px;width:430px;list-style:none}
.bullets li{position:relative;padding-left:27px;margin-bottom:6px;font-size:12.5px;line-height:19.5px;color:var(--muted)}
.bullets li svg{position:absolute;left:0;top:5px}

/* partners */
.partners{left:0;top:2288px;width:1200px;height:397px;background:var(--lime);overflow:hidden}
.partner-panel{left:327px;top:202px;width:873px;height:137px;background:#fff}
.center{text-align:center;width:1200px;left:0}

/* news */
.news-img{position:absolute;top:2862px;width:346px;height:232px;border-radius:14px}
.news-body{position:absolute;top:3054px;width:276px;height:165px;background:#fff;box-shadow:0 4px 14px rgba(0,0,0,.08);border-radius:4px;padding:22px 17px}
.date{display:inline-block;background:var(--red);color:#fff;font-size:11px;padding:1px 18px;border-radius:2px}
.meta{display:inline-flex;gap:6px;align-items:center;font-size:11px;color:#777;margin-left:18px}
.news-title{font-size:15px;margin:10px 0 4px}

/* newsletter + footer */
.newsletter{left:0;top:3293px;width:1200px;height:131px;background:var(--teal)}
.footer{left:0;top:3424px;width:1200px;height:309px;background:var(--teal);color:#fff;border-top:2px dotted rgba(255,255,255,.35)}
.footer h4{font-size:17px;font-weight:400;margin-bottom:10px}
.footer li{list-style:none;font-size:12px;line-height:22.6px}
.copyright{left:0;top:3733px;width:1200px;height:41px;background:var(--lime);color:#fff;font-size:12px;text-align:center;line-height:41px}
</style>
</head>
<body>

<!-- top bar -->
<div class="abs topbar">
  <div class="item" style="left:500px"><svg width="14" height="14" viewBox="0 0 24 24"><path fill="#fff" d="M6.6 10.8a15 15 0 0 0 6.6 6.6l2.2-2.2a1 1 0 0 1 1-.25 11.4 11.4 0 0 0 3.6.57 1 1 0 0 1 1 1V20a1 1 0 0 1-1 1A17 17 0 0 1 3 4a1 1 0 0 1 1-1h3.5a1 1 0 0 1 1 1c0 1.25.2 2.45.57 3.57a1 1 0 0 1-.25 1z"/></svg>04-5550123</div>
  <div class="item" style="left:670px"><svg width="12" height="15" viewBox="0 0 24 30"><path fill="#fff" d="M12 0a10 10 0 0 0-10 10c0 7.5 10 20 10 20s10-12.5 10-20A10 10 0 0 0 12 0zm0 14a4 4 0 1 1 0-8 4 4 0 0 1 0 8z"/></svg>Alem 12/4 POB 4410 Netanya, 42150</div>
  <div class="item" style="left:975px"><svg width="18" height="13" viewBox="0 0 24 17"><rect width="24" height="17" rx="2" fill="#fff"/><path d="M1 1l11 8 11-8" stroke="#0b6360" stroke-width="2" fill="none"/></svg>selamkaveh@mailbox.example</div>
</div>

<!-- nav -->
<header class="abs nav">
  <div class="brand"><div class="mark"></div><span>Selam Kaveh</span></div>
  <nav class="menu">
    <a class="active" style="left:312px">Home</a>
    <a style="left:379px">About Us <b style="color:var(--red)">+</b></a>
    <a style="left:488px">The Community</a>
    <a style="left:620px">News <b style="color:var(--red)">+</b></a>
    <a style="left:699px">Advocacy</a>
    <a style="left:800px">Partners</a>
    <a style="left:889px">Supports Us</a>
  </nav>
  <div class="pill-btn nav-cta"><span class="ic"><svg width="16" height="16" viewBox="0 0 24 24"><path fill="var(--teal)" d="M6.6 10.8a15 15 0 0 0 6.6 6.6l2.2-2.2a1 1 0 0 1 1-.25 11.4 11.4 0 0 0 3.6.57 1 1 0 0 1 1 1V20a1 1 0 0 1-1 1A17 17 0 0 1 3 4a1 1 0 0 1 1-1h3.5a1 1 0 0 1 1 1c0 1.25.2 2.45.57 3.57a1 1 0 0 1-.25 1z"/></svg></span>CONTACT US</div>
</header>

<!-- hero -->
<section class="abs hero">
  <div class="abs photo" role="img" aria-label="Crowd of community members waving flags at a street march" style="left:0;top:0;width:1200px;height:638px;background:linear-gradient(160deg,#c9cdd3 0%,#8d8a8c 35%,#6c4a47 60%,#3c3a48 100%)"></div>
  <svg class="abs" style="left:0;top:0" width="1200" height="638">
    <circle cx="940" cy="210" r="420" fill="var(--red)" opacity=".9"/>
    <rect x="1040" y="340" width="170" height="72" rx="36" fill="none" stroke="#d7c93a" stroke-width="2" transform="rotate(-28 1120 376)"/>
  </svg>
  <div class="abs hero-kicker">Welcome to</div>
  <h1 class="abs hero-title">Your Marcy Can Change<br>Someone’s Life</h1>
  <div class="abs pill-btn hero-cta"><span class="ic"><svg width="16" height="16" viewBox="0 0 24 24"><path fill="var(--teal)" d="M6.6 10.8a15 15 0 0 0 6.6 6.6l2.2-2.2a1 1 0 0 1 1-.25 11.4 11.4 0 0 0 3.6.57 1 1 0 0 1 1 1V20a1 1 0 0 1-1 1A17 17 0 0 1 3 4a1 1 0 0 1 1-1h3.5a1 1 0 0 1 1 1c0 1.25.2 2.45.57 3.57a1 1 0 0 1-.25 1z"/></svg></span>CONTACT US</div>
  <div class="abs arrow" style="left:71px;top:337px"><svg width="10" height="12" viewBox="0 0 10 12"><path d="M8 1L2 6l6 5" stroke="#222" stroke-width="2" fill="none"/></svg></div>
  <div class="abs arrow" style="left:1091px;top:337px"><svg width="10" height="12" viewBox="0 0 10 12"><path d="M2 1l6 5-6 5" stroke="#222" stroke-width="2" fill="none"/></svg></div>
</section>

<!-- about -->
<section>
  <svg class="abs" style="left:150px;top:834px" width="410" height="396">
    <circle cx="125" cy="105" r="86" fill="none" stroke="var(--red)" stroke-width="3"/>
    <path d="M121 200 C121 60 190 2 260 2 C340 2 405 70 405 170 C405 300 330 394 250 394 C180 394 121 320 121 200Z" fill="#8c8377"/>
    <circle cx="94" cy="262" r="92" fill="#9aa3ad"/>
  </svg>
  <div class="abs" role="img" aria-label="Photo collage of immigrant families at a rally" style="left:152px;top:836px;width:405px;height:392px"></div>
  <div class="abs eyebrow" style="left:672px;top:836px">Welcome to</div>
  <h2 class="abs h2" style="left:672px;top:858px">Selam Kaveh</h2>
  <p class="abs body-text" style="left:672px;top:906px;width:390px">Aliyah (immigration) from Ethiopia to Israel and the transition to a sedentary lifestyle has resulted in the emergence of chronic diseases, in particular diabetes.</p>
  <div class="abs stat-val" style="left:672px;top:980px">0.4%</div>
  <div class="abs stat-val" style="left:785px;top:980px">2</div>
  <div class="abs stat-val" style="left:898px;top:980px">18%</div>
  <div class="abs stat-lab" style="left:672px;top:1010px">Immigrants</div>
  <div class="abs stat-lab" style="left:785px;top:1010px">Diabetes</div>
  <div class="abs stat-lab" style="left:898px;top:1010px">General population</div>
  <p class="abs body-text" style="left:672px;top:1046px;width:390px">Selam Kaveh was founded in 1999 by Dr. Miriam Levin, Head of the Endocrinology Unit at the Carmel Valley Medical Center. Her experience with Ethiopian patients made her realize that medical treatment could not succeed without culturally competent communication.</p>
  <div class="abs pill-btn" style="left:672px;top:1160px;width:150px"><span class="ic"><svg width="14" height="14" viewBox="0 0 14 14"><path d="M2 2l5 5-5 5M7 2l5 5-5 5" stroke="var(--teal)" stroke-width="1.6" fill="none"/></svg></span>LEARN MORE</div>
</section>

<!-- programs -->
<section>
  <svg class="abs" style="left:0;top:1308px" width="600" height="450">
    <path d="M0 0 H300 C420 0 480 90 520 150 C450 150 420 260 420 330 C420 400 380 450 330 450 H0Z" fill="var(--teal)"/>
  </svg>
  <div class="abs eyebrow" style="left:631px;top:1308px">Programs</div>
  <h2 class="abs h2" style="left:631px;top:1330px">Our Programs</h2>
  <div class="prog-card" role="img" aria-label="Woman presenting at a health education session" style="left:154px;background:linear-gradient(160deg,#8fa4bf,#4c5d7a)"></div>
  <div class="prog-card" role="img" aria-label="Visitors at a regional health fair" style="left:394px;background:linear-gradient(160deg,#c9ccd3,#6f5d5f)"></div>
  <div class="prog-card" role="img" aria-label="Community marchers with flags for the Amharic radio program" style="left:633px;background:linear-gradient(160deg,#b6bfc9,#8d5a5a)"></div>
  <div class="prog-card" role="img" aria-label="Volunteers at a health leadership workshop" style="left:873px;background:linear-gradient(160deg,#d7dde3,#5a86a8)"></div>
  <div class="prog-card" role="img" aria-label="Health resource supplies being distributed" style="left:1113px;background:linear-gradient(160deg,#c9a67a,#8f6a4c)"></div>
  <div class="prog-title" style="left:155px;color:#fff">Health Education<br>Presentation</div>
  <div class="prog-title" style="left:395px;color:#fff">Regional Health<br>Fairs</div>
  <div class="prog-title" style="left:635px">Amharic Radio<br>Program</div>
  <div class="prog-title" style="left:875px">Health Leadership<br>Development</div>
  <div class="prog-title" style="left:1115px">Health Resources</div>
  <div class="abs pager"><span>01</span><span>02</span><span>03</span><span style="display:flex;align-items:center;gap:8px;color:var(--red)"><i style="display:block;width:30px;height:2px;background:var(--red)"></i>04</span></div>
</section>

<!-- community -->
<section>
  <div class="abs eyebrow" style="left:129px;top:1841px">The Community</div>
  <h2 class="abs h2" style="left:129px;top:1863px">Health &amp; Community</h2>
  <p class="abs body-text" style="left:129px;top:1911px;width:400px">Today the Ethiopian Israeli community numbers over 120,000 with new immigrants still continuing to arrive. For many, immigration led to the disintegration of.</p>
  <ul class="abs bullets">
    <li><svg width="14" height="14" viewBox="0 0 14 14"><path d="M7 0l3 3-3 3-3-3zM7 8l3 3-3 3-3-3zM0 7l3-3 3 3-3 3zM8 7l3-3 3 3-3 3z" fill="var(--teal)"/></svg>Only 48% of Ethiopian patients say they understand medical staff, compared to 92% of others surveyed.</li>
    <li><svg width="14" height="14" viewBox="0 0 14 14"><path d="M7 0l3 3-3 3-3-3zM7 8l3 3-3 3-3-3zM0 7l3-3 3 3-3 3zM8 7l3-3 3 3-3 3z" fill="var(--teal)"/></svg>82% of Ethiopian patients understand little or nothing of the pharmacists’ instructions, compared with 20% of others</li>
    <li><svg width="14" height="14" viewBox="0 0 14 14"><path d="M7 0l3 3-3 3-3-3zM7 8l3 3-3 3-3-3zM0 7l3-3 3 3-3 3zM8 7l3-3 3 3-3 3z" fill="var(--teal)"/></svg>55% state they understand little or nothing of the advice given by dieticians.</li>
    <li><svg width="14" height="14" viewBox="0 0 14 14"><path d="M7 0l3 3-3 3-3-3zM7 8l3 3-3 3-3-3zM0 7l3-3 3 3-3 3zM8 7l3-3 3 3-3 3z" fill="var(--teal)"/></svg>Patients who view their illness as totally debilitating and withdraw from family responsibilities,</li>
  </ul>
  <div class="abs pill-btn" style="left:129px;top:2180px;width:148px"><span class="ic"><svg width="14" height="14" viewBox="0 0 14 14"><path d="M2 2l5 5-5 5M7 2l5 5-5 5" stroke="var(--teal)" stroke-width="1.6" fill="none"/></svg></span>LEARN MORE</div>
  <svg class="abs" style="left:730px;top:1820px" width="370" height="400">
    <circle cx="100" cy="70" r="58" fill="#6e0a0a"/>
    <circle cx="208" cy="334" r="58" fill="#6e0a0a"/>
    <circle cx="266" cy="143" r="95" fill="none" stroke="var(--lime)" stroke-width="2"/>
    <circle cx="178" cy="205" r="169" fill="#b9b0b2"/>
  </svg>
  <div class="abs" role="img" aria-label="Crowd holding red and white flags under a large banner" style="left:739px;top:1856px;width:338px;height:338px;border-radius:50%;background:radial-gradient(circle at 50% 35%,#e9e4e4 0%,#c9464a 45%,#8a6f74 100%)"></div>
</section>

<!-- partners -->
<section class="abs partners">
  <svg class="abs" style="left:0;top:0" width="1200" height="397">
    <path d="M-40 80 C20 60 60 200 84 250 C100 290 60 300 20 280" fill="none" stroke="#7d0c0c" stroke-width="2"/>
    <path d="M842 200 C860 60 1080 40 1113 200" fill="none" stroke="#7d0c0c" stroke-width="2"/>
    <path d="M880 339 L905 397 M1172 339 L1198 397" stroke="#7d0c0c" stroke-width="2"/>
  </svg>
  <div class="abs eyebrow center" style="top:68px;color:#fff">Partners</div>
  <h2 class="abs h2 center" style="top:90px">What You Can DO</h2>
  <p class="abs center" style="top:133px;font-size:12.5px;line-height:19.5px;color:#fff">Selam Kaveh non-profit organization operates to promote the ethiopian israel<br>communinty healthcare, using donations and govermant funding.</p>
  <div class="abs partner-panel">
    <div class="abs" style="left:55px;top:40px;width:46px;height:56px;border:2px solid #c0504d;border-radius:4px"></div>
    <div class="abs" style="left:160px;top:54px;width:110px;height:22px;background:#5fa94b;border-radius:11px"></div>
    <div class="abs" style="left:322px;top:36px;width:64px;height:64px;background:#2b7ec1;border-radius:50%"></div>
    <div class="abs" style="left:452px;top:30px;width:54px;height:82px;background:#3d5fa0;border-radius:6px"></div>
    <div class="abs" style="left:567px;top:40px;width:78px;height:58px;background:#3fa7c9;border-radius:8px"></div>
    <div class="abs" style="left:712px;top:47px;width:72px;height:40px;background:#4b4f9c;border-radius:4px"></div>
  </div>
</section>

<!-- news -->
<section>
  <div class="abs eyebrow center" style="top:2775px">Updated</div>
  <h2 class="abs h2 center" style="top:2798px">Latest News</h2>
  <div class="news-img" role="img" aria-label="Group of women holding a non profit sign" style="left:236px;background:linear-gradient(160deg,#e6e3df,#b07a6b)"></div>
  <div class="news-img" role="img" aria-label="Volunteers serving water at a community health day" style="left:618px;background:linear-gradient(160deg,#c8d3da,#6f8aa1)"></div>
  <article class="news-body" style="left:272px">
    <span class="date">Jan 7,2021</span><span class="meta"><svg width="18" height="12" viewBox="0 0 18 12"><ellipse cx="9" cy="6" rx="8" ry="5" fill="none" stroke="var(--lime)" stroke-width="1.5"/><circle cx="9" cy="6" r="2.5" fill="var(--lime)"/></svg>5</span><span class="meta"><svg width="14" height="12" viewBox="0 0 14 12"><path d="M1 1h12v7H6l-3 3V8H1z" fill="none" stroke="var(--red)" stroke-width="1.3"/></svg>5</span>
    <h3 class="news-title" style="font-weight:400">Diabetes Voice</h3>
    <p class="body-text" style="font-size:12px">Lorem Ipsum is simply dummy text of the printing and typesetting industry. Lorem Ipsum has</p>
  </article>
  <article class="news-body" style="left:654px">
    <span class="date">Jan 7,2021</span><span class="meta"><svg width="18" height="12" viewBox="0 0 18 12"><ellipse cx="9" cy="6" rx="8" ry="5" fill="none" stroke="var(--lime)" stroke-width="1.5"/><circle cx="9" cy="6" r="2.5" fill="var(--lime)"/></svg>5</span><span class="meta"><svg width="14" height="12" viewBox="0 0 14 12"><path d="M1 1h12v7H6l-3 3V8H1z" fill="none" stroke="var(--red)" stroke-width="1.3"/></svg>5</span>
    <h3 class="news-title" style="font-weight:400">Diabetes Voice</h3>
    <p class="body-text" style="font-size:12px">Lorem Ipsum is simply dummy text of the printing and typesetting industry. Lorem Ipsum has</p>
  </article>
</section>

<!-- newsletter -->
<section class="abs newsletter">
  <h3 class="abs" style="left:190px;top:55px;font-size:29px;font-weight:500;color:#fff">Newsletter Subscribe</h3>
  <div class="abs" style="left:545px;top:55px;width:445px;height:45px;border:1px solid #fff;border-radius:23px">
    <span class="abs" style="left:15px;top:13px;font-size:12px;color:#fff">Enter Your Email Address...</span>
    <span class="abs" style="left:307px;top:3px;width:133px;height:37px;border-radius:19px;background:var(--lime);font-size:13px;font-weight:600;text-align:center;line-height:37px">SUBSRIBE</span>
  </div>
</section>

<!-- footer -->
<footer class="abs footer">
  <div class="abs" style="left:62px;top:55px;display:flex;align-items:center;gap:8px">
    <div style="width:40px;height:40px;border-radius:50%;background:#fff"></div>
    <span style="font-size:15px;font-weight:600">Selam Kaveh</span>
  </div>
  <div class="abs" style="left:337px;top:40px">
    <h4>Site Map</h4>
    <ul><li>- Home</li><li>- About Us</li><li>- The Community</li><li>- Programs</li><li>- News</li><li>- Advocacy</li><li>- Partners</li><li>- Supports</li></ul>
  </div>
  <div class="abs" style="left:612px;top:40px;width:250px">
    <h4>Contact Us</h4>
    <svg class="abs" style="left:0;top:42px" width="15" height="15" viewBox="0 0 24 24"><path fill="#fff" d="M6.6 10.8a15 15 0 0 0 6.6 6.6l2.2-2.2a1 1 0 0 1 1-.25 11.4 11.4 0 0 0 3.6.57 1 1 0 0 1 1 1V20a1 1 0 0 1-1 1A17 17 0 0 1 3 4a1 1 0 0 1 1-1h3.5a1 1 0 0 1 1 1c0 1.25.2 2.45.57 3.57a1 1 0 0 1-.25 1z"/></svg>
    <div class="abs" style="left:33px;top:40px;font-size:12px;line-height:19px">Phone<br>04-5550123</div>
    <svg class="abs" style="left:2px;top:100px" width="12" height="15" viewBox="0 0 24 30"><path fill="#fff" d="M12 0a10 10 0 0 0-10 10c0 7.5 10 20 10 20s10-12.5 10-20A10 10 0 0 0 12 0zm0 14a4 4 0 1 1 0-8 4 4 0 0 1 0 8z"/></svg>
    <div class="abs" style="left:33px;top:98px;width:215px;font-size:12px;line-height:19px">Office<br>Alem 12/4 POB 4410 Netanya, 42150</div>
    <svg class="abs" style="left:0;top:177px" width="18" height="13" viewBox="0 0 24 17"><rect width="24" height="17" rx="2" fill="#fff"/><path d="M1 1l11 8 11-8" stroke="#0b6360" stroke-width="2" fill="none"/></svg>
    <div class="abs" style="left:33px;top:173px;font-size:12px;line-height:19px">Email<br>selamkaveh@mailbox.example</div>
  </div>
  <div class="abs" style="left:888px;top:40px;width:220px;font-size:12px;line-height:19px">
    <h4>Selam Kaveh</h4>
    <p>Selam means peace in Amharic, and also signifies a woven basket; an expensive and unique gift to preserve.</p>
    <p style="margin-top:6px">Kaveh means health in Hebrew.</p>
    <p style="margin-top:11px">Health is a gift to be preserved</p>
  </div>
</footer>
<div class="abs copyright">Copyright © 2022 SELAM KAVEH- All Right Reserved.</div>

</body>
</html>
```